Modern business card design for professional copywriter

I'd like a business card design that I can use to have my cards printed out by tavrel.com as a squared corners business card (see artwork and design guidelines here: https://help.tavrel.com/hc/en-gb/sections/300481762-TAVREL-Product-Templates)

The design should be clean and modern and reflect the colours, tone and branding on my website: https://gretafolvane.com.au

Target Market(s)

Professionals, B2B small business owners

Industry/Entity Type

Business

Contact Information for Business Card

Greta Folvane
m: 0427 954 368
e: greta@gretafolvane.com.au
w: gretafolvane.com.au

Font styles to use
Sans Serif

Requirements
Must have
• Tagline: "Smart copywriting for clever business people"
• Brand colours: fd8000, 009984, 666666 and black
Nice to have

```html
<!DOCTYPE html>
<html lang="en">
<head>
<meta charset="utf-8">
<title>Greta Folvane – Business Card</title>
<link href="https://fonts.googleapis.com/css2?family=Outfit:wght@300;400;500;600&display=swap" rel="stylesheet">
<style>
  :root {
    --orange: #f5821f;
    --teal: #179a84;
    --grey: #666666;
    --text-grey: #555555;
    --white: #ffffff;
    --edge: #cfcfcf;
  }
  * { margin: 0; padding: 0; box-sizing: border-box; }
  html, body { width: 1200px; height: 1200px; overflow: hidden; background: var(--white); }
  body { position: relative; font-family: "Outfit", sans-serif; }

  .card { position: absolute; }

  /* Front */
  .card-front {
    left: 224px; top: 62px; width: 756px; height: 489px;
    background: var(--white); border: 1px solid var(--edge);
  }
  .side-stripe { position: absolute; left: 48px; width: 20px; }
  .side-stripe--orange { top: 0; height: 246px; background: var(--orange); }
  .side-stripe--teal { top: 246px; height: 190px; background: var(--teal); }
  .side-stripe--grey { top: 436px; height: 53px; background: var(--grey); }

  .brand-name {
    position: absolute; left: 200px; top: 112px;
    display: flex; align-items: center; gap: 16px;
    font-size: 64px; font-weight: 500; color: var(--teal); letter-spacing: -1px;
    line-height: 1;
  }
  .brand-mark { width: 18px; height: 18px; background: var(--orange); }

  .tagline {
    position: absolute; left: 97px; top: 232px;
    font-size: 19px; font-weight: 500; color: var(--text-grey);
    letter-spacing: 2.2px; text-transform: uppercase; white-space: nowrap;
  }

  .contact-name {
    position: absolute; left: 98px; top: 312px;
    font-size: 31px; font-weight: 400; color: var(--orange); letter-spacing: -0.5px;
  }
  .contact-list { position: absolute; left: 100px; top: 356px; list-style: none; }
  .contact-item {
    display: flex; align-items: center; gap: 11px; height: 31px;
    font-size: 22px; font-weight: 300; color: var(--text-grey); letter-spacing: 1px;
  }
  .contact-icon {
    width: 23px; height: 23px; border-radius: 50%;
    display: flex; align-items: center; justify-content: center;
    color: var(--white); font-size: 15px; font-weight: 500; line-height: 1; letter-spacing: 0;
  }
  .contact-icon--mobile { background: var(--orange); }
  .contact-icon--email { background: var(--grey); }
  .contact-icon--web { background: var(--teal); }

  /* Back */
  .card-back {
    left: 224px; top: 598px; width: 763px; height: 514px;
    background: var(--teal);
  }
  .tagline-frame {
    position: absolute; left: 108px; top: 192px; width: 547px; height: 130px;
    border: 1px solid rgba(255,255,255,0.85);
    display: flex; flex-direction: column; align-items: center; justify-content: center;
  }
  .tagline-line {
    font-size: 35px; font-weight: 500; color: var(--white);
    letter-spacing: 2.6px; line-height: 42px; text-transform: uppercase; white-space: nowrap;
  }
  .tagline-accent { color: var(--orange); font-weight: 600; }
</style>
</head>
<body>

  <section class="card card-front">
    <div class="side-stripe side-stripe--orange"></div>
    <div class="side-stripe side-stripe--teal"></div>
    <div class="side-stripe side-stripe--grey"></div>

    <div class="brand-name"><span class="brand-mark"></span>Greta Folvane</div>

    <p class="tagline">Smart copywriting for clever business people</p>

    <h1 class="contact-name">Greta Folvane</h1>
    <ul class="contact-list">
      <li class="contact-item"><span class="contact-icon contact-icon--mobile">m</span>0427. 954. 368</li>
      <li class="contact-item"><span class="contact-icon contact-icon--email">e</span>greta@gretafolvane.com.au</li>
      <li class="contact-item"><span class="contact-icon contact-icon--web">w</span>gretafolvane.com.au</li>
    </ul>
  </section>

  <section class="card card-back">
    <div class="tagline-frame">
      <p class="tagline-line"><span class="tagline-accent">Smart</span> copywriting for</p>
      <p class="tagline-line"><span class="tagline-accent">Clever</span> business people</p>
    </div>
  </section>

</body>
</html>
```